Local Restaurant Needs a One Page Breakfast Menu

I own a restaurant and we are going to be starting a new breakfast service. I want a one page menu that is clean, bright, and tongue in cheek. We will only have a limited menu, so there should be plenty of space to work with. I will not want actual food pictures, but more of a cartoon style representations of food. I'd like a modern cartoon style mixed with our current 1950s theme.

Name of Restaurant: Dorrity's
Location: 2493 W. Larch. Quillmont, ND 58214 - Phone: 620-555-3047 (including location is not a requirement)

Breakfast Hours: 6:30 am - 10:30 am

The two colors selected below are not required, but they are the two colors that are featured inside the dining room of the restaurant.

Industry/Entity Type

Restaurant

Colors
8667ad
acd036

Requirements
Must have
• Menu must only be one page (either standard letter or oversized - either would be ok).

Menu items:

Stuffed Omellete. Stuffing choices: cheese, peppers, jalapenos, onions, tomatoes, salsa, sour cream, green onions, sausage, bacon, ham

Dorrity's Blintz (thin, stuffed, pancakes): Stuffing choices: chocolate chips, Q&Zs, Talbot's Nibbles, strawberries, blueberries, raspberries, bananas, sour cream

Homemade Coffee Cake

Cinnamon Rolls

Beverages - Coffee, Soda, Milk

Prices not set (use placeholders).

```html
<!DOCTYPE html>
<html lang="en">
<head>
<meta charset="utf-8">
<title>Dorrity's Breakfast Menu</title>
<link rel="stylesheet" href="https://fonts.googleapis.com/css2?family=Federo&family=Poiret+One&display=swap">
<style>
  :root {
    --menu-red: #a81e27;
    --banner-white: #ffffff;
    --ink-dark: #1c0b0b;
    --text-light: #ffffff;
    --dot: #111111;
  }
  html, body {
    margin: 0;
    padding: 0;
    overflow: hidden;
  }
  .menu {
    position: relative;
    width: 927px;
    height: 1200px;
    background: var(--menu-red);
    overflow: hidden;
    font-family: "Poiret One", sans-serif;
    color: var(--text-light);
  }
  .banner {
    position: absolute;
    left: 0;
    top: 0;
  }
  .brand-name {
    position: absolute;
    left: 140px;
    width: 650px;
    top: 22px;
    margin: 0;
    text-align: center;
    font-family: "Federo", sans-serif;
    font-weight: 400;
    font-size: 108px;
    line-height: 1;
    color: var(--menu-red);
  }
  .hours {
    position: absolute;
    top: 243px;
    left: 0;
    width: 917px;
    text-align: center;
    font-size: 27px;
    font-weight: 700;
    letter-spacing: 0.6px;
    word-spacing: 3px;
    color: var(--ink-dark);
    margin: 0;
  }
  .item {
    position: absolute;
    left: 70px;
    width: 800px;
  }
  .item-title {
    margin: 0;
    height: 48px;
    white-space: nowrap;
    font-weight: 400;
    line-height: 1;
  }
  .title-text {
    display: inline-block;
    font-family: "Federo", sans-serif;
    font-size: 48px;
    text-transform: uppercase;
    transform: scaleX(0.81);
    transform-origin: left center;
  }
  .item-note {
    position: absolute;
    top: 18px;
    font-size: 22px;
    font-weight: 700;
    letter-spacing: 0.4px;
  }
  .item-desc {
    margin: 10px 0 0;
    font-size: 24px;
    font-weight: 700;
    line-height: 38px;
    letter-spacing: 0.6px;
    word-spacing: 3px;
  }
  .price {
    position: absolute;
    top: 10px;
    right: 12px;
    font-family: "Federo", sans-serif;
    font-size: 28px;
  }
  .price sup {
    font-size: 17px;
    vertical-align: 12px;
  }
  .dot-rule {
    position: absolute;
    left: 82px;
    width: 786px;
    height: 10px;
    background: radial-gradient(circle, var(--dot) 3.2px, transparent 3.8px) repeat-x;
    background-size: 16.4px 10px;
  }
  .footer {
    position: absolute;
    top: 1138px;
    left: 0;
    width: 927px;
    text-align: center;
    font-size: 22px;
    font-weight: 700;
    color: var(--ink-dark);
    margin: 0;
    word-spacing: 1px;
  }
  .footer .sep {
    display: inline-block;
    margin: 0 36px;
    font-size: 26px;
  }
</style>
</head>
<body>
<main class="menu">
  <svg class="banner" width="927" height="230" viewBox="0 0 927 230" aria-hidden="true">
    <polygon points="140,0 790,0 790,172 457,218 140,172" fill="var(--banner-white)"/>
    <g fill="var(--dot)">
      <circle cx="120" cy="22" r="4"/><circle cx="120" cy="40" r="4"/><circle cx="120" cy="58" r="4"/>
      <circle cx="120" cy="76" r="4"/><circle cx="120" cy="94" r="4"/><circle cx="120" cy="112" r="4"/>
      <circle cx="120" cy="130" r="4"/><circle cx="120" cy="148" r="4"/>
      <circle cx="808" cy="28" r="4"/><circle cx="808" cy="46" r="4"/><circle cx="808" cy="64" r="4"/>
      <circle cx="808" cy="82" r="4"/><circle cx="808" cy="100" r="4"/><circle cx="808" cy="118" r="4"/>
      <circle cx="808" cy="136" r="4"/><circle cx="808" cy="154" r="4"/>
    </g>
  </svg>
  <h1 class="brand-name">Dorrity's</h1>

  <p class="hours">Breakfast Served 6:30am - 10:30am</p>

  <section class="item" style="top:342px">
    <h2 class="item-title"><span class="title-text">Stuffed Omellete</span></h2>
    <span class="price">$7.<sup>99</sup></span>
    <p class="item-desc">Stuffing choices: cheese, peppers, jalapenos, onions, tomatoes, salsa, sour cream, green onions, sausage, bacon, ham</p>
  </section>
  <div class="dot-rule" style="top:503px"></div>

  <section class="item" style="top:548px">
    <h2 class="item-title"><span class="title-text">Dorrity's Blintz</span><span class="item-note" style="left:345px">(thin, stuffed, pancakes)</span></h2>
    <span class="price" style="right:18px">$7.<sup>99</sup></span>
    <p class="item-desc">Stuffing choices: chocolate chips, Q&amp;Zs, Talbot's Nibbles, strawberries, blueberries, raspberries, bananas, sour cream</p>
  </section>
  <div class="dot-rule" style="top:707px"></div>

  <section class="item" style="top:748px">
    <h2 class="item-title"><span class="title-text">Homemade Coffee Cake</span></h2>
    <span class="price">$7.<sup>99</sup></span>
  </section>
  <div class="dot-rule" style="top:825px"></div>

  <section class="item" style="top:864px">
    <h2 class="item-title"><span class="title-text">Cinnamon Rolls</span></h2>
    <span class="price">$7.<sup>99</sup></span>
  </section>
  <div class="dot-rule" style="top:952px"></div>

  <section class="item" style="top:994px">
    <h2 class="item-title"><span class="title-text">Beverages</span></h2>
    <span class="price">$7.<sup>99</sup></span>
    <p class="item-desc" style="margin-top:4px">Coffee, Soda, Milk.</p>
  </section>

  <p class="footer">2493 W. Larch, Quillmont, ND 58214<span class="sep">&bull;</span>Phone: 620-555-3047</p>
</main>
</body>
</html>
```